Global Expert Network Firm needs business card design

We need business card design for a new company based in Seoul, South Korea called 'Corwell Insight Partners'. We recruit industry experts covering all countries and connect our client and recruited expert by phone, face-to-face meetings and etc. We are a global expert network firm that is focused on delivering high-quality experts to our clients throughout the world. Our clients include multinational corporations, global consulting firms, private equity firms, venture capital firms, asset management companies.
We have made new logo and please find attachment.(Please use new logo)
Target Market(s)
Global Consulting Firms, Investment Firms, Private Equity Firms, Venture Capital Firms.
Industry/Entity Type
Recruitment
Contact Information for Business Card
We need two Languages (English and Korean Version).
The front is Korean and the back is English version.
[The back] [English]
Company Name: Corwell Insight Partners, Inc.
CEO Name: Daniel Park
Address: #507, Hanbit Bldg, 82 Maebongsan-ro, Dobong-gu, Seoul, 01327, Korea
Tel. +82 2 718 4052
Fax. +82 2 864 1097
Mobile. +82 10 7264 8815
Email: daniel@corwellip.com
Web: www.corwellip.com
[The front] [Korean] => Described in same order as English version.
회사명: 코웰인사이트파트너스(주)
대표이사: 박도현
주소: 서울시 도봉구 매봉산로 82 한빛빌딩 507호
Tel. 02 718 4052
Fax. 02 864 1097
Mobile. 010 7264 8815
Web: www.corwellip.com
Look and feel
Each slider illustrates characteristics of the customer's brand and the style your logo design should communicate.

```html
<!DOCTYPE html>
<html lang="en">
<head>
<meta charset="utf-8">
<title>Corwell Insight Partners – Business Cards</title>
<link href="https://fonts.googleapis.com/css2?family=Roboto:wght@400;500&family=Noto+Sans+KR:wght@400;500&display=swap" rel="stylesheet">
<style>
  :root {
    --backdrop: #bcbcbc;
    --navy: #13214b;
    --paper: #f3f3f1;
    --on-navy: #ffffff;
    --on-navy-soft: #dfe3ee;
    --ink: #13214b;
  }
  * { margin: 0; padding: 0; box-sizing: border-box; }
  html, body { width: 1200px; height: 576px; overflow: hidden; }
  body {
    background: var(--backdrop);
    font-family: "Roboto", "Noto Sans KR", sans-serif;
    position: relative;
  }
  .card {
    position: absolute;
    top: 139px;
    width: 484px;
    height: 291px;
    border-radius: 14px;
    overflow: hidden;
  }
  .card--english { left: 82px; background: var(--navy); color: var(--on-navy); }
  .card--korean { left: 602px; background: var(--paper); color: var(--ink); font-family: "Noto Sans KR", "Roboto", sans-serif; }

  .wordmark {
    position: absolute;
    left: 322px;
    top: 30px;
    font-family: "Roboto", sans-serif;
    font-weight: 400;
    font-size: 21px;
    line-height: 31px;
    letter-spacing: 1px;
    text-transform: uppercase;
  }
  .card--english .wordmark { color: var(--on-navy); }
  .card--korean .wordmark { color: var(--ink); }

  .notch {
    position: absolute;
    left: -13px;
    top: 151px;
    width: 26px;
    height: 26px;
    border-radius: 50%;
  }
  .card--english .notch { background: var(--paper); }
  .card--korean .notch { background: var(--navy); }

  .person {
    position: absolute;
    left: 24px;
    top: 153px;
    white-space: nowrap;
  }
  .person__name { font-size: 17px; font-weight: 400; }
  .person__title { font-size: 10px; margin-left: 3px; }

  .company {
    position: absolute;
    left: 24px;
    top: 195px;
    font-size: 14.5px;
    white-space: nowrap;
  }
  .divider {
    position: absolute;
    left: 24px;
    top: 218px;
    width: 436px;
    height: 1px;
  }
  .card--english .divider { background: var(--on-navy-soft); }
  .card--korean .divider { background: var(--ink); left: 24px; width: 436px; }

  .contact {
    position: absolute;
    left: 24px;
    top: 226px;
    font-size: 10.4px;
    line-height: 15px;
    white-space: nowrap;
  }
  .card--korean .contact { left: 22px; }
  .contact__row { display: flex; align-items: center; }
  .contact__item { display: inline-flex; align-items: center; margin-right: 11px; }
  .icon { width: 9px; height: 9px; margin-right: 10px; fill: currentColor; }
</style>
</head>
<body>

<svg width="0" height="0" style="position:absolute" aria-hidden="true">
  <symbol id="icon-phone" viewBox="0 0 10 10"><path d="M1 3.5 Q5 0.5 9 3.5 L8 5 L6.5 4.2 L6.5 3.3 Q5 2.8 3.5 3.3 L3.5 4.2 L2 5 Z M2.5 6 H7.5 L8.5 9 H1.5 Z"/></symbol>
  <symbol id="icon-fax" viewBox="0 0 10 10"><path d="M3 0.5 H7 V3 H3 Z M1 3.5 H9 V7.5 H1 Z M3 7 H7 V9.5 H3 Z"/></symbol>
  <symbol id="icon-mobile" viewBox="0 0 10 10"><path d="M3 0.5 H7.5 V9.5 H3 Z M3.8 1.6 V7.6 H6.7 V1.6 Z"/></symbol>
  <symbol id="icon-mail" viewBox="0 0 10 10"><path d="M0.5 2 H9.5 L5 5.3 Z M0.5 3 L5 6.4 L9.5 3 V8 H0.5 Z"/></symbol>
  <symbol id="icon-web" viewBox="0 0 10 10"><path d="M5 0.5 A4.5 4.5 0 1 0 5.01 0.5 Z M5 1.4 A1.6 3.6 0 1 0 5.01 1.4 Z M1.2 4.6 H8.8 V5.4 H1.2 Z" fill-rule="evenodd"/></symbol>
</svg>

<section class="card card--english" aria-label="English side">
  <div class="wordmark">Corwell<br>Insight<br>Partners</div>
  <span class="notch"></span>
  <div class="person"><span class="person__name">Daniel Park</span><span class="person__title">CEO &amp; Founder</span></div>
  <div class="company">Corwell Insight Partners, Inc.</div>
  <div class="divider"></div>
  <div class="contact">
    <div class="contact__row">#507, Hanbit Bldg, 82 Maebongsan-ro, Dobong-gu, Seoul, 01327, Korea</div>
    <div class="contact__row">
      <span class="contact__item"><svg class="icon"><use href="#icon-phone"/></svg>+82 2 718 4052</span>
      <span class="contact__item"><svg class="icon"><use href="#icon-fax"/></svg>+82 2 864 1097</span>
      <span class="contact__item"><svg class="icon"><use href="#icon-mobile"/></svg>+82 10 7264 8815</span>
    </div>
    <div class="contact__row">
      <span class="contact__item"><svg class="icon"><use href="#icon-mail"/></svg>daniel@corwellip.com</span>
      <span class="contact__item"><svg class="icon"><use href="#icon-web"/></svg>www.corwellip.com</span>
    </div>
  </div>
</section>

<section class="card card--korean" aria-label="Korean side" lang="ko">
  <div class="wordmark">Corwell<br>Insight<br>Partners</div>
  <span class="notch"></span>
  <div class="person"><span class="person__name">박도현</span><span class="person__title">대표이사</span></div>
  <div class="company">회사명: 코웰인사이트파트너스(주)</div>
  <div class="divider"></div>
  <div class="contact">
    <div class="contact__row">서울시 도봉구 매봉산로 82 한빛빌딩 507호</div>
    <div class="contact__row">
      <span class="contact__item"><svg class="icon"><use href="#icon-phone"/></svg>+02 718 4052</span>
      <span class="contact__item"><svg class="icon"><use href="#icon-fax"/></svg>+02 864 1097</span>
      <span class="contact__item"><svg class="icon"><use href="#icon-mobile"/></svg>+010 7264 8815</span>
    </div>
    <div class="contact__row">
      <span class="contact__item"><svg class="icon"><use href="#icon-mail"/></svg>daniel@corwellip.com</span>
      <span class="contact__item"><svg class="icon"><use href="#icon-web"/></svg>www.corwellip.com</span>
    </div>
  </div>
</section>

</body>
</html>
```